Business Coach needs an elegant business card design

I need a business card design based around my logo for color and to look like a millionaire dollar coach. Incorporate the color of my logo with something creative and attractive that stands out. I am focused on high end companies and the card must look and feel that way.

Target Market(s)

High End Companies and Business Owners - Training People to become millionaires

Industry/Entity Type

Business

Requirements
Must have
• Front -
Logo (attached file) - Website (marlowkeeve.com) - Name (Marlow Keeve) Phone (555.201.7746) - Email (marlow@marlowkeeve.com) (My Title - Success Coach)
Back -
Slogan - Vision (see it) . Action (do it) . Transformation (be it)
Website - Learn More @ marlowkeeve.com

Creative High End Look!
Nice to have
Should not have
• Cheap standard look
nothing traditional

```html
<!DOCTYPE html>
<html lang="en">
<head>
<meta charset="utf-8">
<title>Marlow Keeve Coaching – Business Card</title>
<link rel="stylesheet" href="https://fonts.googleapis.com/css2?family=Cinzel:wght@400&family=Questrial&display=swap">
<style>
  :root {
    --bg: #e8e8eb;
    --back-top: #8d8e95;
    --back-bottom: #4f5057;
    --front-top: #5c5c60;
    --front-bottom: #121213;
    --ink-light: #ececee;
    --ink-soft: #c9c9cd;
    --ink-muted: #a9aab0;
    --ring-back: rgba(255,255,255,0.10);
    --ring-front: rgba(255,255,255,0.09);
  }
  * { margin: 0; padding: 0; box-sizing: border-box; }
  html, body { width: 1200px; height: 720px; overflow: hidden; background: var(--bg); }
  .canvas { position: relative; width: 1200px; height: 720px; background: var(--bg); }

  .card {
    position: absolute;
    width: 540px; height: 309px;
    border-radius: 3px;
    overflow: hidden;
    box-shadow: 0 6px 18px rgba(0,0,0,0.18);
  }
  .card--back  { left: 40px;  top: 205px; background: linear-gradient(160deg, var(--back-top), var(--back-bottom)); }
  .card--front { left: 620px; top: 205px; background: linear-gradient(200deg, var(--front-top), var(--front-bottom) 70%); }

  .ring { position: absolute; border-radius: 50%; }
  .card--back .ring  { width: 300px; height: 300px; right: -70px; top: -40px; border: 26px solid var(--ring-back); }
  .card--front .ring { width: 280px; height: 280px; left: -40px; bottom: -170px; border: 24px solid var(--ring-front); }

  .brand { position: absolute; display: flex; align-items: center; color: var(--ink-light); font-family: "Cinzel", serif; font-weight: 400; }
  .brand__dot { border: 2px solid var(--ink-light); border-radius: 50%; flex: none; }
  .brand__name { line-height: 1; letter-spacing: 0.04em; }
  .brand__sub { display: block; letter-spacing: 0.35em; text-align: center; }

  .card--back .brand { left: 40px; top: 96px; gap: 16px; }
  .card--back .brand__dot { width: 62px; height: 62px; }
  .card--back .brand__name { font-size: 34px; }
  .card--back .brand__sub { font-size: 15px; margin-top: 6px; }

  .slogan {
    position: absolute; left: 0; right: 0; top: 212px;
    text-align: center; font-family: "Questrial", sans-serif;
    color: var(--ink-soft); font-size: 15px; line-height: 1.55; letter-spacing: 0.02em;
  }

  .card--front .brand { left: 28px; top: 40px; gap: 9px; }
  .card--front .brand__dot { width: 36px; height: 36px; }
  .card--front .brand__name { font-size: 17px; }
  .card--front .brand__sub { font-size: 8px; margin-top: 3px; }

  .person { position: absolute; left: 262px; top: 36px; font-family: "Cinzel", serif; color: var(--ink-light); }
  .person__name { font-size: 28px; font-weight: 400; letter-spacing: 0.03em; }
  .person__title { font-family: "Cinzel", serif; font-size: 13px; color: var(--ink-soft); text-transform: none; margin-top: 2px; }

  .contacts { position: absolute; left: 262px; top: 168px; list-style: none; font-family: "Questrial", sans-serif; color: var(--ink-light); font-size: 19px; }
  .contacts li { display: flex; align-items: center; gap: 12px; height: 31px; }
  .contacts svg { width: 15px; height: 15px; flex: none; }
</style>
</head>
<body>
<main class="canvas">

  <section class="card card--back" aria-label="Card back">
    <div class="ring" aria-hidden="true"></div>
    <div class="brand">
      <span class="brand__dot" aria-hidden="true"></span>
      <div>
        <div class="brand__name">Marlow Keeve</div>
        <span class="brand__sub">Coaching</span>
      </div>
    </div>
    <p class="slogan">
      Vision (see it) . Action (do it) . Transformation (be it)<br>
      Learn More @marlowkeeve.com
    </p>
  </section>

  <section class="card card--front" aria-label="Card front">
    <div class="ring" aria-hidden="true"></div>
    <div class="brand">
      <span class="brand__dot" aria-hidden="true"></span>
      <div>
        <div class="brand__name">Marlow Keeve</div>
        <span class="brand__sub">Coaching</span>
      </div>
    </div>

    <div class="person">
      <h1 class="person__name">MARLOW KEEVE</h1>
      <p class="person__title">Success Coach</p>
    </div>

    <ul class="contacts">
      <li>
        <svg viewBox="0 0 16 16" aria-hidden="true"><circle cx="8" cy="8" r="7" fill="none" stroke="#ececee" stroke-width="1.2"/><path d="M5.5 4.5l1.3 1.6-.8 1c.5 1.1 1.3 1.9 2.4 2.4l1-.8 1.6 1.3-.9 1.2c-2.6-.4-4.7-2.5-5.1-5.1z" fill="#ececee"/></svg>
        555.201.7746
      </li>
      <li>
        <svg viewBox="0 0 16 16" aria-hidden="true"><rect x="1" y="3.5" width="14" height="9" fill="#ececee"/><path d="M1 3.5l7 5 7-5" fill="none" stroke="#2a2a2c" stroke-width="1"/></svg>
        marlow@marlowkeeve.com
      </li>
      <li>
        <svg viewBox="0 0 16 16" aria-hidden="true"><circle cx="8" cy="8" r="6.5" fill="none" stroke="#ececee" stroke-width="1.2"/><ellipse cx="8" cy="8" rx="2.8" ry="6.5" fill="none" stroke="#ececee" stroke-width="1"/><path d="M1.5 8h13" stroke="#ececee" stroke-width="1"/></svg>
        www.marlowkeeve.com
      </li>
    </ul>
  </section>

</main>
</body>
</html>
```